SaaS Early tech startup business card design

Unique design for experience ecommerce platform company. the business cards will be used by executive members. conformance with color code is required.

```html
<!DOCTYPE html>
<html lang="en">
<head>
<meta charset="utf-8">
<title>Norvik business card</title>
<link href="https://fonts.googleapis.com/css2?family=Roboto:wght@400;700&display=swap" rel="stylesheet">
<style>
  :root {
    --backdrop: #1d1d1e;
    --card: #2b2a2b;
    --card-dark: #252425;
    --pattern-light: #323132;
    --brand: #1a8fb8;
    --brand-blue: #1475ab;
    --accent-teal: #16b8a0;
    --rule: #17699a;
    --text-light: #d8d8d8;
  }
  * { box-sizing: border-box; margin: 0; padding: 0; }
  html, body {
    width: 1200px; height: 874px; overflow: hidden;
    background: var(--backdrop);
    font-family: "Roboto", Arial, sans-serif;
  }
  .canvas { position: relative; width: 1200px; height: 874px; }
  .card {
    position: absolute; left: 280px; width: 640px; height: 366px;
    background: var(--card);
    box-shadow: 0 18px 40px rgba(0,0,0,0.45);
    overflow: hidden;
  }
  .card--front { top: 50px; }
  .card--back { top: 458px; }

  .front-pattern {
    position: absolute; inset: 0;
    background: linear-gradient(135deg, var(--pattern-light) 0%, var(--card) 50%, var(--card-dark) 100%);
  }
  .wordmark {
    color: var(--brand);
    font-weight: 700;
    letter-spacing: -2px;
    line-height: 1;
  }
  .card--front .wordmark {
    position: absolute; left: 0; right: 0; top: 118px;
    text-align: center; font-size: 118px;
  }

  .card--back .wordmark {
    position: absolute; left: 60px; top: 140px; font-size: 78px;
  }
  .divider {
    position: absolute; left: 336px; top: 84px; width: 1px; height: 200px;
    background: var(--rule);
  }
  .contact {
    position: absolute; left: 362px; top: 88px;
    color: var(--text-light);
  }
  .contact__name {
    color: var(--brand-blue); font-weight: 700; font-size: 24px; line-height: 1.1;
  }
  .contact__role {
    color: var(--accent-teal); font-weight: 700; font-size: 15px; margin-bottom: 10px;
  }
  .contact__address { font-size: 14px; line-height: 1.35; margin-bottom: 10px; }
  .contact__list { list-style: none; font-size: 14px; line-height: 1.45; }
  .contact__list li { display: flex; align-items: center; gap: 9px; }
  .contact__list svg { width: 13px; height: 13px; flex: none; fill: var(--accent-teal); }
</style>
</head>
<body>
<main class="canvas">
  <section class="card card--front">
    <div class="front-pattern" role="img" aria-label="Subtle dark checkered square pattern across the card face"></div>
    <div class="wordmark">norvik</div>
  </section>

  <section class="card card--back">
    <div class="wordmark">norvik</div>
    <div class="divider"></div>
    <div class="contact">
      <p class="contact__name">Daniel Reyes</p>
      <p class="contact__role">President</p>
      <p class="contact__address">214 Alder Court<br>Juneau, Alaska 99801</p>
      <ul class="contact__list">
        <li><svg viewBox="0 0 16 16" aria-hidden="true"><path d="M3 1l3 3-2 2c1 2 3 4 5 5l2-2 3 3-2 3C7 14 2 9 1 3z"/></svg>555-014-2231</li>
        <li><svg viewBox="0 0 16 16" aria-hidden="true"><path d="M4 0h8v16H4zM5.5 1.5v11h5v-11z"/></svg>555-018-7742</li>
        <li><svg viewBox="0 0 16 16" aria-hidden="true"><path d="M4 1h8v4H4zM1 6h14v7h-3v2H4v-2H1zM5 11v3h6v-3z"/></svg>555-019-3360</li>
        <li><svg viewBox="0 0 16 16" aria-hidden="true"><path d="M1 3h14v10H1zM2.5 4.5L8 9l5.5-4.5z"/></svg>hello@norvik.io</li>
        <li><svg viewBox="0 0 16 16" aria-hidden="true"><circle cx="8" cy="8" r="7"/></svg>www.norvik.io</li>
      </ul>
    </div>
  </section>
</main>
</body>
</html>
```